Small Cafe, hidden in an office building, needs a menu layout, to help it stand out.

So we need a menu layout for a very small cafe that can work for both customers in the cafe, as well as being handed out to local businesses. Boring, I know. Well here's some things to give direction and make it more fun.
1. It's an American Korean hybrid. American sandwiches and subs but also Korean dishes including Korean Style Chicken Wings. Her wings are amazing! No, even better then what you just thought.
2. I'm American born, & my wife who runs the cafe, was born in Seoul Korea. I had been toying with the thought of incorporating the Korean flag into a logo. I will attach the images to try and make it clearer.
3. It's called "Harbor Nook Cafe" no, we didn't name it, but what can you do eh? Anywho, the acronym for it is HNC. So we have been using the line, "The main ingredient in great food is the HNC." That doesn't have to stay but I dunno, kinda clever.
4. It has to stay professional kinda because we are in an office building, however my wife has a good sense of humor and laughs a lot. She tries to make it fun and not stuffy by joking around with the customers. They all love her smile and upbeat nature.
5. We are located in College Park MD close to Ashgrove Valley University in an office building, but we both wish we were out in West Virginia in the country.
6. One of her main dishes as far a popularity, is her Korean chicken wings and it just so happens we both love Roosters. Long story... and we do espresso... I'm imagining a coffee drinking rooster with his eyes bugged out on his caffeine buzz. Maybe it's just the fear of the fryer...
7. I thought today, "It sucks we're cooped up in the back of the lobby." ha... ahhhh... I need sleep.
8. I'm including a place holder I made for the website back when we were thinking of calling it PelicanBay Chicken. The Korean flag with it's meanings that are associated with my drawing of a possible logo... Did I mention I need a log designed too? Huh... Ok, well I attached the logo I was thinking about ripping off as the basis of that Idea. I'm not sold on it. It's just something my pea sized brain came up with. I have also attached a picture of my wife at the cafe that way you can get a vibe of her and the place. The menu items. Lastly a picture of a Rooster that I just simply love. I adjusted him in Photoshop and just love the color. Not sure about him making an appearance on the menu... just kinda showing him off I guess. I said I needed sleep right?...
Thanks for reading. Rule the roost!
-Corwin

```html
<!DOCTYPE html>
<html lang="en">
<head>
<meta charset="utf-8">
<title>Harbor Nook Cafe – Menu</title>
<link rel="stylesheet" href="https://fonts.googleapis.com/css2?family=Carlito:wght@400;700&family=Ribeye&display=swap">
<style>
  :root{
    --paper:#f3f1c3;
    --ink:#111111;
    --red:#e21d1a;
    --fold:#d8d6a8;
    --taupe:#c3a28c;
    --chick:#e3130f;
    --prints:#ece23a;
  }
  *{margin:0;padding:0;box-sizing:border-box}
  html,body{width:1200px;height:856px;overflow:hidden;background:var(--paper)}
  body{font-family:"Carlito",Calibri,sans-serif;color:var(--ink)}
  .menu{position:relative;width:1200px;height:856px;background:var(--paper);overflow:hidden}
  .fold{position:absolute;top:0;bottom:0;width:0;border-left:2px dashed var(--fold)}
  .fold--one{left:393px}
  .fold--two{left:786px}
  .panel{position:absolute;top:0;height:856px;text-align:center}
  .panel--korean{left:0;width:396px}
  .panel--breakfast{left:393px;width:393px}
  .panel--info{left:786px;width:414px}
  .section-title{font-family:"Ribeye",cursive;color:var(--red);font-weight:400;font-size:17px;letter-spacing:.5px;text-transform:uppercase;margin-top:37px;line-height:22px}
  .dish{font-size:18px;line-height:20px}
  .dish__name{font-weight:700}
  .panel--korean .dish{margin:20px auto 0;width:282px}
  .panel--korean .dish + .dish{margin-top:40px}
  .panel--breakfast .dish{font-size:18px;line-height:22px;margin-top:20px}
  .panel--breakfast .dish + .dish{margin-top:21px}
  .drinks-title{font-family:"Ribeye",cursive;color:var(--red);font-weight:400;font-size:15px;position:absolute;left:0;width:393px;top:530px;text-align:center}
  .drinks{position:absolute;left:62px;top:552px;border-collapse:collapse;font-size:17px;line-height:21.3px}
  .drinks th,.drinks td{font-weight:400;text-align:left;padding:0}
  .drinks .col-name{width:152px}
  .drinks .col-med{width:62px}
  .tagline{position:absolute;left:0;top:20px;overflow:visible}
  .tagline text{font-family:"Ribeye",cursive;fill:var(--red);font-size:16px}
  .brand{position:absolute;left:55px;top:170px;width:300px;height:360px;display:flex;flex-direction:column;align-items:center;justify-content:center;gap:22px}
  .brand__dot{width:150px;height:150px;border-radius:50%;background:var(--taupe)}
  .brand__name{font-size:34px;font-weight:700;color:var(--ink)}
  .phone{position:absolute;top:593px;left:0;width:414px;font-size:35px;font-weight:700}
  .details{position:absolute;top:654px;left:0;width:414px;font-size:17px;line-height:21px}
  .details strong{display:block}
  .details .address{margin-top:19px}
  .details .web{margin-top:19px}
  .art-rooster{position:absolute;left:45px;top:632px;width:195px;height:190px;border-radius:40% 30% 20% 30%;background:var(--chick)}
  .art-prints{position:absolute;left:245px;top:796px;width:170px;height:52px;border-radius:20px;background:var(--prints);opacity:.7}
</style>
</head>
<body>
<main class="menu">
  <div class="fold fold--one"></div>
  <div class="fold fold--two"></div>

  <section class="panel panel--korean">
    <h2 class="section-title">Korean Favorites</h2>
    <div class="dish">
      <div class="dish__name">Chicken Wings (8)</div>
      <div>Korean Chicken Wings are juicy, spicy, &amp; sweet, &amp; impossible to just eat one. Made with Marisol's homemade sauce!</div>
      <div>7.99</div>
    </div>
    <div class="dish">
      <div class="dish__name">Bibimbap</div>
      <div>Multiple mixed Vegetables, Rice, a Fried Egg &amp; Chili Pepper Paste.</div>
      <div>9.99</div>
    </div>
    <div class="dish">
      <div class="dish__name">Beef BBQ Bulgogi</div>
      <div>Sliced marinated Beef with Onion, Carrot, Zucchini, Green &amp; Red peppers.</div>
      <div>9.99</div>
    </div>
    <div class="dish">
      <div class="dish__name">Spicy Pork Bulgogi</div>
      <div>Daeji Bulgogi is sliced marinated Pork, cooked with Vegetables &amp; served on Rice.</div>
      <div>9.99</div>
    </div>
    <div class="art-rooster" role="img" aria-label="Red rooster illustration pecking at the ground"></div>
    <div class="art-prints" role="img" aria-label="Trail of small yellow chicken footprints"></div>
  </section>

  <section class="panel panel--breakfast">
    <h2 class="section-title">Breakfast</h2>
    <div class="dish"><div class="dish__name">Egg &amp; Cheese Sandwich</div><div>2.99</div></div>
    <div class="dish"><div class="dish__name">Sausage, Egg &amp; Cheese Sandwich</div><div>3.59</div></div>
    <div class="dish"><div class="dish__name">Bacon, Egg &amp; Cheese Sandwich</div><div>3.59</div></div>
    <div class="dish"><span class="dish__name">Bagel &amp; Cream Cheese</span> 1.99</div>
    <div class="dish"><span class="dish__name">Veggie Omelet</span> 4.49</div>
    <div class="dish"><span class="dish__name">Western Omelet</span> 5.29</div>
    <div class="dish"><span class="dish__name">Classic Platter</span> 4.49</div>
    <div class="dish"><span class="dish__name">French Toast Platter</span> 4.49</div>
    <div class="dish"><span class="dish__name">Home Fries</span> 2.25</div>

    <h3 class="drinks-title">DRINKS</h3>
    <table class="drinks">
      <tr><th class="col-name"></th><th class="col-med">Med</th><th>Large</th></tr>
      <tr><td>Americano</td><td>2.19</td><td>2.69</td></tr>
      <tr><td>Cuppaccino</td><td>3.19</td><td>3.49</td></tr>
      <tr><td>Cafe Latte</td><td>3.19</td><td>3.49</td></tr>
      <tr><td>Cafe Mocha</td><td>3.49</td><td>3.79</td></tr>
      <tr><td>Coffee</td><td>1.89</td><td>1.99</td></tr>
      <tr><td>Hot Chocolate</td><td>2.49</td><td>2.79</td></tr>
      <tr><td>Chai Tea Latte</td><td>3.49</td><td>3.79</td></tr>
      <tr><td>Iced Coffee</td><td>1.89</td><td>1.99</td></tr>
      <tr><td>Espresso Single</td><td></td><td>1.59</td></tr>
      <tr><td>Espresso Double</td><td></td><td>1.99</td></tr>
      <tr><td>Variety Teas</td><td></td><td>1.79</td></tr>
    </table>
  </section>

  <section class="panel panel--info">
    <svg class="tagline" width="414" height="130" viewBox="0 0 414 130" aria-label="The main ingredient in great food is HNC">
      <defs><path id="tagline-arc" d="M8 116 Q205 -48 402 116"/></defs>
      <text><textPath href="#tagline-arc" startOffset="50%" text-anchor="middle" textLength="415" lengthAdjust="spacing">THE MAIN INGREDIENT IN GREAT FOOD IS HNC</textPath></text>
    </svg>
    <div class="brand">
      <div class="brand__dot"></div>
      <div class="brand__name">Harbor Nook Cafe</div>
    </div>
    <div class="phone">301-555-0147</div>
    <div class="details">
      <strong>Hours</strong>
      <div>Monday - Friday</div>
      <div>7:30am - 4:30pm</div>
      <div class="address">4120 Meadowlark Ave,<br>College Park, MD 20740</div>
      <div class="web">www.harbornookcafe.net</div>
    </div>
  </section>
</main>
</body>
</html>
```